Meridian Cataract Surgery and Cosmetic Eyelid Surgery

We need Three page website design (home page and interior page template with two looks) with accompanying CSS code. 1. Home page, 2. General Eye-Care page, 3. Cosmetic Eyelid Surgery. #2 an #3 would be only slightly different. See below.

The site being redesigned is http://www.bright-lumen.com.

The content will remain consistent with the current site.

Additional graphics will be included, especially a number of "Before and after" photos of patients for the various procedures.

You can see competitive sites here: http://www.findoraq.com/search?q=cosmetic+eyelid+surgury+santa+rosa&ie=utf-8&oe=utf-8&aq=t&client=browser-b&rlz=1R1TTPP_en___US384

The client likes http://www.view-pmr.com, which has a serious look he likes (not necessarily the colors or design). Avoid too many "happy loving couples" and pretty women, on the main page or cataract/general eye-care pages. They are, however, good on the cosmetic pages.

When patients look at the *cosmetic surgery* pages, they can see the pretty women/couples. For *eye surgery* (which is what this is all about) they should see an attractive, active OLDER couple(s) on cataract surgery and refractive surgery pages.

In the US, premium IOL (Intraocular lens - a clear plastic lens that is implanted in the eye; usually done when the natural lens has been removed in a cataract operation) cataract surgery, cosmetic and refractive surgery are not fully paid for by insurance, so patients can afford to pay for it themselves and are more well-off than the normal market.
Updates

Do not use the graphics or look and feel of the current site.  We are looking for a NEW design, not a remix of the old elements.

The new logo is at http://www.artmarketo.com/file.aspx?fileLocation=claritonvisionlogo0.jpg

 
Do NOT use the old logo.  If your submitted design uses the old logo, please fix it and delete the one with the old logo.

Sorry for not making this clearer when we started.

Normal 0 false false false EN-US X-NONE X-NONE I want to see a home page that gives equal billing to general eyecare and cosmetic and RECONSTRUCTIVE eyelid surgery.   General eyecare should be listed first.  This should have the correct Practice name and Logo:   Meridian Sightcare and Cosmetic Eyelid Surgery Center.  The home page should be inviting to both old and young, men and women.  The General eyecare page should have similar appeal.  Cosmetic Page should be decidedly more feminine.  The home page should also highlight Dr. Brennick' s qualification and provide a site map/navigation.

The colors of the logo do not need to be limited to black and white.  The logos MUST be integrated into the design, not just pasted on the page.

Read the brief carefully and pay careful attention to the target markets.

 

vector art uploaded:  logo.ai

Target Market(s)

OLDER men and women. People whose faces, eyes, etc., have an aged look that they want to look younger. ALSO patients who want to have the best possible vision after CATARACT SURGERY. Patients who want Premium IOL'S which give them vision at both distance and near WITHOUT GLASSES. STATE OF THE ART GLAUCOMA SURGERY.

Industry/Entity Type

Plastic

Requirements
Must have
• Easy to read. Some readers may have vision difficulties. Easy to navigate for the elderly market. Cosmetic page may be a little more complex.

```html
<!DOCTYPE html>
<html lang="en">
<head>
<meta charset="utf-8">
<title>Meridian Sightcare and Cosmetic Eyelid Surgery Center</title>
<link href="https://fonts.googleapis.com/css2?family=Arimo:wght@400;700&display=swap" rel="stylesheet">
<style>
:root{
  --black:#000;
  --blue:#1a73e8;
  --link:#1671d6;
  --text:#222;
  --heading:#444;
  --grey-btn:#d2d2d2;
  --grey-text:#444;
  --panel:#fff;
}
*{margin:0;padding:0;box-sizing:border-box}
html,body{width:674px;height:1200px;overflow:hidden}
body{font-family:"Arimo",Arial,sans-serif;color:var(--text);background:linear-gradient(90deg,#c9c9c9,#f2f2f2 6%,#f2f2f2 94%,#c9c9c9);position:relative}
.abs{position:absolute}
.hero{left:0;top:0;width:674px;height:277px;background:var(--black)}
.topbar{left:0;top:0;width:674px;height:51px;background:linear-gradient(#1b1b1b,#050505);border-bottom:1px solid #2a2a2a}
.nav-divider{top:0;width:1px;height:51px;background:#2c2c2c}
.logo{left:28px;top:0;width:189px;height:122px;background:linear-gradient(135deg,#1e7bf0,#0a52d8);display:flex;align-items:center;justify-content:center}
.logo .name{font-size:19px;font-weight:700;color:#111;line-height:1.15}
.nav-link{top:20px;font-size:9px;color:#fff;letter-spacing:.2px;white-space:nowrap}
.pill{display:flex;align-items:center;justify-content:center;border-radius:10px;background:linear-gradient(#2f8cff,#0750c8);color:#0b2f7a;font-size:8px}
.hero-photo{left:430px;top:51px;width:217px;height:226px;background:linear-gradient(90deg,#000 0%,#4a342b 10%,#b89280 22%,#e8cfc0 45%,#f6ece6 70%,#ffffff 100%)}
.hero-text{left:90px;width:330px;text-align:center;color:#fff;white-space:nowrap}
.hero-small{font-size:11px;color:var(--blue)}
.hero-big{font-size:19px;font-weight:700;letter-spacing:.2px}
.panel{left:27px;top:278px;width:620px;height:868px;background:var(--panel);box-shadow:0 0 6px rgba(0,0,0,.15)}
.side-btn{left:40px;width:136px;height:28px;display:flex;align-items:center;justify-content:center;font-size:8.6px;font-weight:700;background:var(--grey-btn);color:var(--grey-text);white-space:nowrap}
.side-btn.active{background:linear-gradient(#2d86f0,#07358c);color:#fff}
.photo{border:4px solid var(--blue);background:linear-gradient(135deg,#cfe0f2,#f2f6fb)}
.h2{font-size:15px;font-weight:700;color:var(--heading);white-space:nowrap}
.body-text{font-size:8.8px;line-height:15.2px;color:var(--text)}
.rule{left:51px;top:435px;width:567px;height:1px;background:#ccc}
.bullet{left:83px;width:8px;height:8px;border-radius:50%;border:1px solid #444;background:radial-gradient(#222 30%,#fff 35%)}
.item{font-size:11.5px;font-weight:700;color:var(--link);white-space:nowrap}
.desc{left:133px;font-size:8.6px;color:var(--text);white-space:nowrap}
.care-btn{left:90px;width:137px;height:23px;display:flex;align-items:center;justify-content:center;font-size:8.5px;font-weight:700;color:#fff;background:linear-gradient(#2f87f5,#062f85)}
.footer{left:0;top:1147px;width:674px;height:53px;background:#0a0a0a;color:#8a8a8a;font-size:7px;display:flex;align-items:center;justify-content:center}
</style>
</head>
<body>
<div class="abs hero"></div>
<div class="abs topbar"></div>
<div class="abs nav-divider" style="left:437px"></div>

<div class="abs hero-photo" role="img" aria-label="Close-up portrait photograph of a woman's eye and brow"></div>

<div class="abs logo"><span class="name">Meridian<br>Sightcare</span></div>

<div class="abs pill" style="left:241px;top:18px;width:60px;height:16px;color:#0c2e72">HOME</div>
<div class="abs nav-link" style="left:326px">GENERAL EYE-CARE</div>
<div class="abs nav-link" style="left:457px">COSMETIC EYELID SUGERY</div>

<div class="abs hero-text" style="top:134px"><div class="hero-small">WELCOME TO</div></div>
<div class="abs hero-text" style="top:150px"><div class="hero-big">LARKFIELD VALLEY EYE CARE</div></div>
<div class="abs hero-text" style="top:180px"><div class="hero-small">AND THE</div></div>
<div class="abs hero-text" style="top:196px"><div class="hero-big">AESTHETIC SURGERY CENTER</div></div>
<div class="abs pill" style="left:72px;top:238px;width:76px;height:20px">READ MORE</div>

<div class="abs panel"></div>

<div class="abs side-btn active" style="top:292px">PATIENT PHOTOS</div>
<div class="abs side-btn" style="top:323px;font-size:8px">ABOUT DR. ROBERT BRENNICK</div>
<div class="abs side-btn" style="top:355px">MAP TO OUR OFFICE</div>
<div class="abs side-btn" style="top:386px">CONTACT US</div>

<div class="abs photo" style="left:197px;top:294px;width:143px;height:91px" role="img" aria-label="Photograph of a smiling medical team in white coats"></div>
<div class="abs h2" style="left:354px;top:304px">OUR MISSION</div>
<div class="abs body-text" style="left:355px;top:326px;width:262px">Is to provide personal, friendly, state of the art general eye care as well as the latest advances in cosmetic eyelid surgery for men and women.</div>

<div class="abs rule"></div>

<div class="abs photo" style="left:40px;top:460px;width:174px;height:94px" role="img" aria-label="Photograph of a woman's face marked for cosmetic eyelid surgery"></div>
<div class="abs h2" style="left:237px;top:460px">EYELID AND FACIAL COSMETIC SURGERY</div>
<div class="abs body-text" style="left:225px;top:489px;width:358px;text-indent:23px">Dr Brennick specializes in cosmetic and reconstructive laser surgery of the eyelids and upper face. Because he performs the procedures with super-pulsed carbon dioxide lasers, his patients enjoy less bruising and swelling and are back to work (or play) sooner.</div>
<div class="abs body-text" style="left:53px;top:571px;width:478px">Dr. Brennick is one of an elite rank of 400 surgeons nationally who are trained in the reconstruction and beautification of eyelids. Following his residency in Ophthalmology, Dr. Brennick was awarded a formal fellowship in eyelid plastic and orbital surgery (One of only 30 nationwide). Is cosmetic eyelid or facial plastic surgery right for you? Enter here to learn more about how cosmetic eyelid surgery can help you.</div>

<div class="abs bullet" style="top:663px"></div>
<div class="abs item" style="left:109px;top:661px">Cosmetic Eyelid Surgery For Men and Women</div>
<div class="abs bullet" style="top:682px"></div>
<div class="abs item" style="left:109px;top:680px">How Aesthetic Eyelid Surgery is Performed</div>
<div class="abs bullet" style="top:701px"></div>
<div class="abs item" style="left:119px;top:699px">Upper Eyelids:</div>
<div class="abs desc" style="top:721px">Advanced laser eyelid surgery precisely removes bulges and wrinkles and allows for less bruising and faster recuperation.</div>
<div class="abs bullet" style="top:739px"></div>
<div class="abs item" style="left:119px;top:737px">Lower Eyelids</div>
<div class="abs desc" style="top:759px">Bags under eyes can often be removed without visible incisions.</div>
<div class="abs bullet" style="top:777px"></div>
<div class="abs item" style="left:119px;top:775px">Forehead/Brow</div>
<div class="abs desc" style="top:797px">Endoscopic Brow Lift improves brow/forehead position and contour with only small incisions.</div>
<div class="abs bullet" style="top:815px"></div>
<div class="abs item" style="left:119px;top:813px">Laser Skin Resurfacing</div>
<div class="abs desc" style="top:835px">Ideal for removing wrinkles around the eyes and mouth. Your complexion looks years younger!</div>

<div class="abs h2" style="left:65px;top:867px">General Eye Care</div>
<div class="abs body-text" style="left:70px;top:892px;width:545px">Robert A. Brennick, MD is certified by the National Board of Eye Medicine and is a member of the Guild of Ocular Surgeons. He is an expert in the management of cataracts, glaucoma, diabetic retinopathy, dry eye problems and thyroid eye disease. If you would like more information about diseases of the eye and their treatments, look here.</div>

<div class="abs care-btn" style="top:944px">CATARACTS</div>
<div class="abs care-btn" style="top:972px">DIABETIC RETIMOPTHY</div>
<div class="abs care-btn" style="top:1000px">FLASHES AND FLOATERS</div>
<div class="abs care-btn" style="top:1028px">GLAUCOMA</div>
<div class="abs care-btn" style="top:1057px">MACULAR DEGENERATION</div>

<div class="abs body-text" style="left:70px;top:1089px;white-space:nowrap">If you would like to find out more about the office and scheduling appointments</div>
<div class="abs pill" style="left:432px;top:1102px;width:59px;height:16px;font-size:6px;color:#fff">READ MORE</div>

<div class="abs footer">Copyright 2010. Larkfield Valley. All rights reserved.</div>
</body>
</html>
```